Empresa de tecnología busca diseño de tarjetas de presentación

Se requiere tarjeta de presentación impresa, con los datos de contacto y logo de la empresa. (se adjunta una imagen como referencia, esto no significa que deberá de ser igual)

```html
<!DOCTYPE html>
<html lang="es">
<head>
<meta charset="utf-8">
<title>Vireo TI — Tarjeta de presentación</title>
<link href="https://fonts.googleapis.com/css2?family=Poppins:wght@300;400;600;700&display=swap" rel="stylesheet">
<style>
  :root {
    --navy: #14336b;
    --navy-deep: #0f2a5c;
    --lime: #9bc53d;
    --white: #ffffff;
    --ink: #1d1d1f;
    --page: #eceef2;
  }
  * { box-sizing: border-box; margin: 0; padding: 0; }
  html, body {
    width: 1200px; height: 863px; overflow: hidden;
    background: var(--page);
    font-family: "Poppins", sans-serif;
  }
  .stage {
    position: relative; width: 1200px; height: 863px;
    display: flex; justify-content: center; align-items: center; gap: 60px;
  }
  .card {
    position: relative; width: 320px; height: 560px; overflow: hidden;
    border-radius: 4px; box-shadow: 0 10px 30px rgba(15, 42, 92, .18);
  }
  .card-bg { position: absolute; inset: 0; }

  /* Front */
  .card--front { background: var(--white); }
  .brand-name {
    position: absolute; top: 38px; left: 0; right: 0; text-align: center;
    color: var(--white); font-weight: 600; font-size: 30px; letter-spacing: 6px;
  }
  .holder { position: absolute; top: 150px; left: 0; right: 0; text-align: center; }
  .holder-name { font-weight: 700; font-size: 22px; color: var(--ink); letter-spacing: .5px; }
  .holder-role { font-weight: 300; font-size: 16px; color: var(--ink); margin-top: 2px; }
  .contacts {
    position: absolute; left: 40px; right: 20px; list-style: none;
    color: var(--ink); font-size: 14px; line-height: 1.35;
  }
  .contacts--main { top: 318px; }
  .contacts--support { top: 470px; }
  .contacts li { display: flex; align-items: flex-start; gap: 10px; margin-bottom: 4px; }
  .contacts svg { flex: none; width: 14px; height: 14px; margin-top: 2px; fill: var(--ink); }
  .ticket-pill {
    position: absolute; top: 432px; left: 34px; right: 34px;
    background: var(--white); border-radius: 14px; padding: 4px 0;
    text-align: center; font-size: 14px; color: var(--ink);
  }

  /* Back */
  .card--back { background: var(--navy); }
  .texture {
    position: absolute; top: 0; left: 0; right: 0; height: 470px;
    background: linear-gradient(180deg, var(--navy) 0%, var(--navy-deep) 50%, var(--navy) 100%);
  }
  .back-mark {
    position: absolute; top: 220px; left: 0; right: 0;
    display: flex; justify-content: center; align-items: center; gap: 14px;
  }
  .back-mark-name { color: var(--lime); font-weight: 600; font-size: 44px; letter-spacing: 6px; }
  .back-mark-dot { width: 22px; height: 22px; border-radius: 50%; background: var(--lime); }
  .website {
    position: absolute; bottom: 34px; left: 0; right: 0; text-align: center;
    color: var(--white); font-size: 15px; letter-spacing: 3px;
  }
</style>
</head>
<body>
<main class="stage">

  <article class="card card--front">
    <svg class="card-bg" viewBox="0 0 320 560" aria-hidden="true">
      <path d="M0 0 H320 V92 Q200 150 0 115 Z" fill="var(--navy)"/>
      <path d="M0 310 Q150 255 320 285 V560 H0 Z" fill="var(--lime)"/>
    </svg>
    <div class="brand-name">Vireo TI</div>
    <div class="holder">
      <h1 class="holder-name">LUCÍA MARVÁN</h1>
      <p class="holder-role">Gerente Marketing Digital</p>
    </div>
    <ul class="contacts contacts--main">
      <li><svg viewBox="0 0 16 16"><path d="M3 1h3l1.5 4-2 1.2a9 9 0 0 0 4.3 4.3L11 8.5l4 1.5v3a2 2 0 0 1-2 2A12 12 0 0 1 1 3a2 2 0 0 1 2-2z"/></svg>(55) 4218 7730 ext.204</li>
      <li><svg viewBox="0 0 16 16"><path d="M4 0h8a1 1 0 0 1 1 1v14a1 1 0 0 1-1 1H4a1 1 0 0 1-1-1V1a1 1 0 0 1 1-1zm1 2v10h6V2zm3 11a1 1 0 1 0 0 2 1 1 0 0 0 0-2z"/></svg>56 2947 6180</li>
      <li><svg viewBox="0 0 16 16"><path d="M1 3h14v10H1zm1.5 1.5L8 9l5.5-4.5z"/></svg>lucia.marvan@vireoti.com</li>
      <li><svg viewBox="0 0 16 16"><path d="M8 0a5.5 5.5 0 0 1 5.5 5.5C13.5 10 8 16 8 16S2.5 10 2.5 5.5A5.5 5.5 0 0 1 8 0zm0 3.5a2 2 0 1 0 0 4 2 2 0 0 0 0-4z"/></svg>Piso 7, Torre Alameda CDMX</li>
    </ul>
    <div class="ticket-pill">¿Necesitas levantar un ticket?</div>
    <ul class="contacts contacts--support">
      <li><svg viewBox="0 0 16 16"><path d="M3 1h3l1.5 4-2 1.2a9 9 0 0 0 4.3 4.3L11 8.5l4 1.5v3a2 2 0 0 1-2 2A12 12 0 0 1 1 3a2 2 0 0 1 2-2z"/></svg>01 800 5106 284</li>
      <li><svg viewBox="0 0 16 16"><path d="M1 3h14v10H1zm1.5 1.5L8 9l5.5-4.5z"/></svg>soporte@vireoti.com</li>
    </ul>
  </article>

  <article class="card card--back">
    <div class="texture" role="img" aria-label="Patrón decorativo de líneas onduladas en azul oscuro"></div>
    <div class="back-mark">
      <span class="back-mark-name">Vireo TI</span>
      <span class="back-mark-dot"></span>
    </div>
    <p class="website">www.VireoTI.com</p>
  </article>

</main>
</body>
</html>
```